Remote Planning & Scheduling Power Point Presentation

This PP presentation is to help explain what RPS is and its benefits. Need help with a better illustration on slide 3 that explains the process, overall aesthetics, need better images, and cleaner workflow on slide 18. Keep the ZOL Logo in the bottom right of each slide. I have included a one-pager and infographic to help. I am still working of verbiage.

Thanks
JR

```html
<!DOCTYPE html>
<html lang="en">
<head>
<meta charset="utf-8">
<title>RPS Flow Process</title>
<link rel="stylesheet" href="https://fonts.googleapis.com/css2?family=Questrial&family=Arimo:wght@700&display=swap">
<style>
  :root {
    --navy: #153184;
    --slate: #47525e;
    --slate-light: #55606c;
    --blue: #2f6fbb;
    --gold: #f5c143;
    --ink: #111111;
    --paper: #ffffff;
    --mark: #b9bec6;
  }
  * { box-sizing: border-box; margin: 0; padding: 0; }
  html, body { width: 1200px; height: 678px; overflow: hidden; background: var(--paper); }
  .slide { position: relative; width: 1200px; height: 678px; background: var(--paper); overflow: hidden; }
  .slide__topline { position: absolute; left: 0; top: 0; width: 1200px; height: 4px; background: #000; }
  .header { position: absolute; left: 46px; top: 49px; width: 1108px; height: 174px; background: var(--navy); overflow: hidden; }
  .header__panel { position: absolute; inset: 0; }
  .header__shadow { position: absolute; left: 46px; top: 223px; width: 1108px; height: 18px; background: linear-gradient(#d9dbe0, rgba(255,255,255,0)); }
  .header__title { position: absolute; left: 77px; top: 52px; font-family: "Questrial", sans-serif; font-size: 47px; color: var(--paper); letter-spacing: 0.5px; }

  .flow { position: absolute; inset: 0; }
  .flow__arrows { position: absolute; left: 0; top: 0; width: 1200px; height: 678px; z-index: 2; }
  .step {
    position: absolute; width: 187px; height: 77px; border-radius: 12px;
    display: flex; align-items: center; gap: 14px; padding-left: 22px;
    font-family: "Arimo", Arial, sans-serif; font-weight: 700; font-size: 20.5px; line-height: 1.17;
    z-index: 1;
  }
  .step--blue { background: var(--blue); color: var(--paper); }
  .step--gold { background: var(--gold); color: var(--ink); }
  .step--pill { border-radius: 40px; }
  .step__icon { width: 46px; height: 46px; flex: none; }
  .step__icon--sm { width: 30px; }
  .step__label { white-space: nowrap; }

  .brand { position: absolute; left: 1072px; top: 609px; font-family: "Arimo", Arial, sans-serif; font-weight: 700; font-size: 30px; color: var(--mark); letter-spacing: 1px; }
</style>
</head>
<body>
<main class="slide">
  <div class="slide__topline"></div>

  <header class="header">
    <svg class="header__panel" viewBox="0 0 1108 174" preserveAspectRatio="none" aria-hidden="true">
      <polygon points="836,0 1108,0 1108,174 718,174" fill="var(--slate)"/>
      <polygon points="1020,0 1108,0 1108,174 960,174" fill="var(--slate-light)" opacity="0.6"/>
    </svg>
    <h1 class="header__title">RPS Flow Process</h1>
  </header>
  <div class="header__shadow"></div>

  <section class="flow">
    <!-- column 1 -->
    <div class="step step--blue step--pill" style="left:55px;top:252px;gap:6px;padding-left:20px">
      <svg class="step__icon step__icon--sm" viewBox="0 0 30 46" fill="none" stroke="currentColor" stroke-width="3"><path d="M15 8v26M6 25l9 9 9-9M4 40h22"/></svg>
      <span class="step__label">On Site</span>
      <svg class="step__icon" viewBox="0 0 46 46" fill="currentColor"><circle cx="14" cy="12" r="5"/><circle cx="32" cy="12" r="5"/><circle cx="23" cy="22" r="5"/><path d="M5 30c0-6 18-6 18 0v4H5zM23 30c0-6 18-6 18 0v4H23zM13 42c0-7 20-7 20 0v3H13z"/></svg>
    </div>
    <div class="step step--blue" style="left:55px;top:355px">
      <svg class="step__icon" viewBox="0 0 46 46" fill="currentColor"><rect x="2" y="8" width="4" height="4"/><rect x="12" y="8" width="32" height="3"/><rect x="2" y="20" width="4" height="4"/><rect x="12" y="20" width="32" height="3"/><rect x="2" y="32" width="4" height="4"/><rect x="12" y="32" width="32" height="3"/></svg>
      <span class="step__label">Collect<br>Worklist</span>
    </div>
    <div class="step step--blue" style="left:55px;top:458px">
      <svg class="step__icon" viewBox="0 0 46 46" fill="none" stroke="currentColor" stroke-width="4"><circle cx="11" cy="28" r="8"/><circle cx="35" cy="28" r="8"/><path d="M19 26h8M6 20l5-8h6l2 12M40 20l-5-8h-6l-2 12"/></svg>
      <span class="step__label">Scope<br>Review</span>
    </div>
    <div class="step step--blue" style="left:55px;top:561px">
      <svg class="step__icon" viewBox="0 0 46 46" fill="none" stroke="currentColor" stroke-width="3"><path d="M8 8h30v30H12a4 4 0 0 1-4-4z"/><path d="M4 8h8v6H4zM15 17h18M15 23h18M15 29h14"/></svg>
      <span class="step__label">Planing<br>Premise</span>
    </div>

    <!-- column 2 -->
    <div class="step step--gold" style="left:317px;top:252px">
      <svg class="step__icon" viewBox="0 0 46 46" fill="none" stroke="currentColor" stroke-width="3"><circle cx="23" cy="23" r="6"/><circle cx="6" cy="7" r="4"/><circle cx="40" cy="7" r="4"/><circle cx="6" cy="39" r="4"/><circle cx="40" cy="39" r="4"/><circle cx="42" cy="23" r="3"/><path d="M9 10l9 8M37 10l-9 8M9 36l9-8M37 36l-9-8M29 23h10"/></svg>
      <span class="step__label">Detail<br>Planning</span>
    </div>
    <div class="step step--gold step--pill" style="left:317px;top:355px;gap:10px;padding-left:10px">
      <svg class="step__icon" viewBox="0 0 46 46" fill="none" stroke="currentColor" stroke-width="3"><circle cx="23" cy="23" r="3"/><path d="M15 14a12 12 0 0 0 0 18M31 14a12 12 0 0 1 0 18M8 8a21 21 0 0 0 0 30M38 8a21 21 0 0 1 0 30"/></svg>
      <span class="step__label">Remort</span>
      <svg class="step__icon" viewBox="0 0 46 46" fill="currentColor"><circle cx="14" cy="12" r="5"/><circle cx="32" cy="12" r="5"/><circle cx="23" cy="22" r="5"/><path d="M5 30c0-6 18-6 18 0v4H5zM23 30c0-6 18-6 18 0v4H23zM13 42c0-7 20-7 20 0v3H13z"/></svg>
    </div>
    <div class="step step--blue" style="left:317px;top:458px">
      <svg class="step__icon" viewBox="0 0 46 46" fill="none" stroke="currentColor" stroke-width="3"><rect x="3" y="12" width="40" height="28" rx="2"/><path d="M15 12l3-5h10l3 5"/><circle cx="23" cy="26" r="9"/><circle cx="23" cy="26" r="5"/></svg>
      <span class="step__label">Field<br>Photos</span>
    </div>
    <div class="step step--blue" style="left:317px;top:561px">
      <svg class="step__icon" viewBox="0 0 46 46" fill="none" stroke="currentColor" stroke-width="3"><rect x="6" y="3" width="34" height="40" rx="3"/><path d="M6 16h34M6 29h34M20 9h6M20 22h6M20 35h6"/></svg>
      <span class="step__label">Data<br>Collection</span>
    </div>

    <!-- column 3 -->
    <div class="step step--gold" style="left:576px;top:252px;gap:16px;padding-left:24px">
      <svg class="step__icon" viewBox="0 0 46 46" fill="currentColor"><path d="M19 2h8l1 6 5 2 5-4 6 6-4 5 2 5 6 1v8l-6 1-2 5 4 5-6 6-5-4-5 2-1 6h-8l-1-6-5-2-5 4-6-6 4-5-2-5-6-1v-8l6-1 2-5-4-5 6-6 5 4 5-2z"/><circle cx="23" cy="23" r="9" fill="var(--gold)"/><circle cx="23" cy="23" r="5"/></svg>
      <span class="step__label">Develop<br>Package</span>
    </div>
    <div class="step step--gold" style="left:576px;top:355px;gap:16px;padding-left:24px">
      <svg class="step__icon" viewBox="0 0 46 46" fill="none" stroke="currentColor" stroke-width="3"><rect x="2" y="4" width="38" height="32"/><path d="M2 11h38M8 17h24M8 23h16M8 29h12"/><circle cx="34" cy="33" r="6" fill="var(--gold)"/><path d="M38 37l6 6"/></svg>
      <span class="step__label">Package<br>Review</span>
    </div>
    <div class="step step--blue" style="left:576px;top:458px;gap:10px;padding-left:10px">
      <svg class="step__icon" viewBox="0 0 46 46" fill="none" stroke="currentColor" stroke-width="3"><path d="M2 10h10l10-4h12l10 2M2 14l14 10 6 6M44 12l-8 16-10 10M10 28l4 4M14 32l4 4M18 36l4 4"/><path d="M22 14h10l4 8"/></svg>
      <span class="step__label">Package<br>Acceptance</span>
    </div>
    <div class="step step--gold" style="left:576px;top:561px;gap:16px;padding-left:18px">
      <svg class="step__icon" viewBox="0 0 46 46" fill="none" stroke="currentColor" stroke-width="3"><rect x="3" y="7" width="40" height="36"/><path d="M3 15h40M13 3v8M33 3v8M9 21h28v16H9zM9 29h28M16 21v16M23 21v16M30 21v16"/></svg>
      <span class="step__label">Level 01</span>
    </div>

    <!-- column 4 -->
    <div class="step step--gold step--pill" style="left:834px;top:352px;gap:14px;padding-left:16px">
      <svg class="step__icon" viewBox="0 0 46 46" fill="none" stroke="currentColor" stroke-width="3"><rect x="3" y="7" width="40" height="36"/><path d="M3 15h40M13 3v8M33 3v8M9 21h28v16H9zM9 29h28M16 21v16M23 21v16M30 21v16"/></svg>
      <span class="step__label">Level 03<br>Schedule</span>
    </div>
    <div class="step step--gold" style="left:834px;top:458px;gap:18px;padding-left:16px">
      <svg class="step__icon" viewBox="0 0 46 46" fill="none" stroke="currentColor" stroke-width="3"><rect x="3" y="7" width="40" height="36"/><path d="M3 15h40M13 3v8M33 3v8M9 21h28v16H9zM9 29h28M16 21v16M23 21v16M30 21v16"/></svg>
      <span class="step__label">Level 02</span>
    </div>
    <div class="step step--blue" style="left:834px;top:561px;gap:14px;padding-left:20px">
      <svg class="step__icon" viewBox="0 0 46 46" fill="currentColor"><ellipse cx="15" cy="11" rx="10" ry="8"/><ellipse cx="32" cy="14" rx="9" ry="7"/><circle cx="13" cy="25" r="5"/><circle cx="33" cy="25" r="5"/><path d="M2 44c0-12 22-12 22 0zM22 44c0-12 22-12 22 0z"/></svg>
      <span class="step__label">Schedule<br>Review</span>
    </div>

    <svg class="flow__arrows" viewBox="0 0 1200 678" aria-hidden="true">
      <!-- down arrows -->
      <polygon fill="var(--blue)" points="123,329 173,329 173,339 184,339 148,355 112,339 123,339"/>
      <polygon fill="var(--blue)" points="123,432 173,432 173,442 184,442 148,458 112,442 123,442"/>
      <polygon fill="var(--blue)" points="123,535 173,535 173,545 184,545 148,561 112,545 123,545"/>
      <polygon fill="var(--gold)" points="644,329 694,329 694,339 705,339 669,355 633,339 644,339"/>
      <polygon fill="var(--gold)" points="644,432 694,432 694,442 705,442 669,458 633,442 644,442"/>
      <polygon fill="var(--blue)" points="644,535 694,535 694,545 705,545 669,561 633,545 644,545"/>
      <!-- up arrows -->
      <polygon fill="var(--blue)" points="385,561 435,561 435,551 446,551 410,535 374,551 385,551"/>
      <polygon fill="var(--blue)" points="385,458 435,458 435,448 446,448 410,432 374,448 385,448"/>
      <polygon fill="var(--gold)" points="385,355 435,355 435,345 446,345 410,329 374,345 385,345"/>
      <polygon fill="var(--blue)" points="902,561 952,561 952,551 963,551 927,535 891,551 902,551"/>
      <polygon fill="var(--gold)" points="902,458 952,458 952,448 963,448 927,429 891,448 902,448"/>
      <!-- right arrows -->
      <polygon fill="var(--blue)" points="241,586 289,586 289,577 317,599 289,622 289,612 241,612"/>
      <polygon fill="var(--gold)" points="504,276 552,276 552,267 576,290 552,312 552,304 504,304"/>
      <polygon fill="var(--gold)" points="763,586 810,586 810,577 834,599 810,622 810,612 763,612"/>
    </svg>
  </section>

  <div class="brand">ZOL</div>
</main>
</body>
</html>
```